Bargo Finch

I want a design for a website where users can insert products URLs from different sites and the user will get notified by email when that product's price changes.

On the homepage I'd like a big input where the user can insert a product's URL. On the same page the following will appear:
- my products that I follow (options: share, buy, unfollow) + it's current price and deviation from last time it's price has changed (I may have many products that I follow, so maybe a table layout would be wise. - just a suggestion)
- products that other people follow (options: follow). If my Chatterloop friends follow a certain product, I can see their photo(eg: friend1, friend2 and 5 others are following this product) (also, may people may follow a product.)

On the login page I can register using user / pass or using Chatterloop

The 3rd page is the product's page. Once I click on any product I go to this page. On this page I can see:
- picture, name and price and no of people following this product
- a chart with the product's price over the last 30 days
- list with friends that follow this product (when logged in)
- product options: follow / unfollow, share, buy

Then I want the design for an email template that I send when 1 or more prices of a user's products change.

Nice to have: want level for product - describes how much wanted is a product after a certain internal algorithm

NB:
- flat design (not really kestra, something more like the new Vyra interface - just a suggestion)
- I'd prefer a red theme (based on the idea that the site will be represented by a rooster)
- don't forget the design for basic elements: loading screen, popup, alert, messages, etc

I've posted an initial prototype with what I'd like the design to contain.

• - flat design
- must be simple. much white space
• as few gradients as possible

```html
<!DOCTYPE html>
<html lang="en">
<head>
<meta charset="utf-8">
<title>Bargo Finch – Friends Products</title>
<link rel="stylesheet" href="https://fonts.googleapis.com/css2?family=Arimo:wght@400;700&display=swap">
<style>
  :root {
    --red: #e3232a;
    --page-grey: #e6e7e6;
    --field-grey: #e5e6e6;
    --text-dark: #58595b;
    --text-mid: #666769;
    --overlay: #c9cacc;
    --overlay-soft: rgba(200, 201, 204, 0.85);
    --white: #ffffff;
  }
  * { box-sizing: border-box; margin: 0; padding: 0; }
  html, body { width: 1200px; height: 1000px; overflow: hidden; }
  body {
    position: relative;
    background: var(--white);
    font-family: "Arimo", Arial, sans-serif;
    color: var(--text-dark);
  }
  .site-header { position: absolute; left: 0; top: 0; width: 1200px; height: 95px; background: var(--white); }
  .brand {
    position: absolute; left: 10px; top: 8px; width: 106px; height: 106px;
    border-radius: 50%; background: var(--red); z-index: 2;
    display: flex; align-items: center; justify-content: center; text-align: center;
    color: var(--white); font-weight: 700; font-size: 21px; line-height: 22px;
  }
  .main-nav a {
    position: absolute; top: 38px; font-size: 27px; color: var(--red); text-decoration: none;
  }
  .main-nav .nav-products { left: 154px; border-bottom: 1.5px solid var(--red); padding-bottom: 2px; }
  .main-nav .nav-contact { left: 336px; }
  .sign-out { position: absolute; left: 1032px; top: 17px; font-size: 21px; color: var(--red); }
  .avatar {
    position: absolute; left: 1120px; top: 9px; width: 46px; height: 39px;
    background: linear-gradient(180deg, #e9eaeb, #cfd1d3);
  }
  .social { position: absolute; top: 56px; width: 35px; height: 35px; border-radius: 50%; background: var(--red); }
  .social-chatterloop { left: 1033px; }
  .social-chirpwave { left: 1080px; }
  .social-snapmosaic { left: 1127px; }

  .page-body { position: absolute; left: 0; top: 95px; width: 1200px; height: 873px; background: var(--page-grey); }

  .tab { position: absolute; font-size: 25px; font-weight: 700; color: var(--text-dark); }
  .tab-mine { left: 132px; top: 160px; }
  .tab-friends {
    left: 325px; top: 143px; width: 219px; height: 72px; background: var(--white);
    padding: 20px 0 0 10px;
  }
  .panel { position: absolute; left: 91px; top: 213px; width: 1009px; height: 649px; background: var(--white); }

  .url-search { position: absolute; left: 157px; top: 324px; width: 885px; height: 71px; display: flex; }
  .url-field {
    position: relative; flex: 1; background: var(--field-grey);
    font-size: 25px; color: var(--text-mid); padding: 23px 0 0 22px;
  }
  .url-field svg { position: absolute; right: 14px; top: 31px; }
  .search-button {
    width: 168px; background: var(--red); color: var(--white);
    font-size: 33px; text-align: center; padding-top: 17px;
  }

  .carousel-arrow { position: absolute; top: 610px; }
  .arrow-prev { left: 113px; }
  .arrow-next { left: 1063px; }

  .product-card { position: absolute; }
  .card-dice { left: 153px; top: 489px; width: 269px; height: 269px;
    background: radial-gradient(circle at 50% 45%, #c3c5c5, #a9abac); }
  .card-socks { left: 461px; top: 487px; width: 275px; height: 274px;
    background: linear-gradient(180deg, #f3f4f4, #e2e3e4); }
  .card-cases { left: 773px; top: 489px; width: 269px; height: 269px;
    background: linear-gradient(135deg, #c9c1b6 0%, #e0a2b8 35%, #7d6a63 60%, #3fb5ab 85%, #b8b2a8 100%); }

  .card-action {
    position: absolute; top: 0; height: 46px; background: var(--overlay);
    color: var(--white); font-size: 25px; text-align: center; padding-top: 10px;
  }
  .action-follow { left: 0; width: 120px; }
  .action-buy { left: 154px; width: 121px; }
  .card-info {
    position: absolute; left: 0; top: 185px; width: 275px; height: 89px;
    background: var(--overlay-soft); color: var(--white);
    font-size: 13px; line-height: 17px; padding: 12px 0 0 13px;
  }
  .pointer { position: absolute; left: 487px; top: 553px; }

  .site-footer { position: absolute; left: 106px; top: 906px; font-size: 16px; color: var(--text-dark); display: flex; gap: 0; }
  .site-footer span.sep { margin: 0 7px; font-size: 10px; line-height: 20px; }
</style>
</head>
<body>
  <header class="site-header">
    <div class="brand">Bargo<br>Finch</div>
    <nav class="main-nav">
      <a class="nav-products" href="#">Products</a>
      <a class="nav-contact" href="#">Contact</a>
    </nav>
    <span class="sign-out">Sign out</span>
    <div class="avatar" role="img" aria-label="User profile picture"></div>
    <span class="social social-chatterloop" role="img" aria-label="Chatterloop"></span>
    <span class="social social-chirpwave" role="img" aria-label="Chirpwave"></span>
    <span class="social social-snapmosaic" role="img" aria-label="Snapmosaic"></span>
  </header>

  <main class="page-body"></main>

  <div class="tab tab-mine">My Products</div>
  <div class="tab tab-friends">Friends Products</div>
  <section class="panel"></section>

  <form class="url-search">
    <div class="url-field">Enter Your Product URL
      <svg width="26" height="26" viewBox="0 0 26 26" aria-hidden="true">
        <circle cx="10" cy="10" r="7" fill="none" stroke="#e3232a" stroke-width="2.6"/>
        <line x1="15" y1="15" x2="23" y2="23" stroke="#e3232a" stroke-width="3.4" stroke-linecap="round"/>
      </svg>
    </div>
    <div class="search-button">Search</div>
  </form>

  <svg class="carousel-arrow arrow-prev" width="18" height="29" viewBox="0 0 18 29" aria-label="Previous"><polygon points="18,0 18,29 0,14.5" fill="#666769"/></svg>
  <svg class="carousel-arrow arrow-next" width="18" height="29" viewBox="0 0 18 29" aria-label="Next"><polygon points="0,0 18,14.5 0,29" fill="#666769"/></svg>

  <div class="product-card card-dice" role="img" aria-label="Product photo: pair of silver dice"></div>

  <div class="product-card card-socks" role="img" aria-label="Product photo: three white low rise socks">
    <div class="card-action action-follow">Follow</div>
    <div class="card-action action-buy">Buy</div>
    <div class="card-info">$14.99<br>Stridelo Low Rise Socks</div>
  </div>

  <div class="product-card card-cases" role="img" aria-label="Product photo: patterned phone cases on a wooden table"></div>

  <svg class="pointer" width="24" height="36" viewBox="0 0 24 36" aria-hidden="true">
    <polygon points="1,1 1,26 7,20 12,33 16,31 11,19 20,19" fill="#111" stroke="#fff" stroke-width="1"/>
  </svg>

  <footer class="site-footer">
    <span>Terms</span><span class="sep">•</span>
    <span>About</span><span class="sep">•</span>
    <span>Privacy</span><span class="sep">•</span>
    <span>Help</span>
  </footer>
</body>
</html>
```